Vexel Business Cards

We need a new look business cvard to refelect our new look website www.vexel-example.com.au
We’re Vexel, a team of town planning and traffic and transport engineering specialists located in Melbourne.

Vexel is a company that is structured, articulate, dynamic, progressive, accurate and adaptable.
Our key messages are:
1. We make your life easier by doing what we do best
2. We tell you what you need to know not what you want to hear
3. Polished and professional but not afraid to show some personality

we would like a bold new look that is polished and professional but not afraid to show a bit of personality

Target Market(s)

Vexel’s diverse client base consists of architecture practices, builders, developers, local government and the legal fraternity.

Industry/Entity Type

Town

Requirements
Must have
• must use our logo and have the following information

Joel Harcastle
Director

Vexel Consultants Pty Ltd
Fernhollow first floor
Tamber Street
Elmsbury VIC 3199 Australia
+61 03 9555 0187
mail@vexel-example.com.au
www.vexel-example.com.au
Nice to have
• We would like to see the logo used or the colours of the logo used.

```html
<!DOCTYPE html>
<html lang="en">
<head>
<meta charset="utf-8">
<title>Vexel Business Cards</title>
<link rel="stylesheet" href="https://fonts.googleapis.com/css2?family=Open+Sans:wght@400;600;700&display=swap">
<style>
  :root {
    --canvas: #ecebe8;
    --card: #ffffff;
    --slate: #5b6470;
    --slate-dark: #4a525d;
    --ink: #3f4650;
    --accent-green: #3f9b45;
    --card-shadow: rgba(40, 40, 40, 0.18);
  }
  * { box-sizing: border-box; margin: 0; padding: 0; }
  html, body {
    width: 1200px;
    height: 720px;
    overflow: hidden;
    background: var(--canvas);
    font-family: "Open Sans", Arial, sans-serif;
    color: var(--ink);
  }
  .canvas {
    width: 1200px;
    height: 720px;
    display: flex;
    align-items: center;
    justify-content: center;
    gap: 40px;
  }
  .card {
    position: relative;
    width: 540px;
    height: 330px;
    background: var(--card);
    box-shadow: 0 6px 18px var(--card-shadow);
    overflow: hidden;
  }

  /* shared wordmark */
  .wordmark {
    display: flex;
    align-items: center;
    justify-content: center;
    gap: 12px;
    color: var(--slate);
    font-weight: 400;
    letter-spacing: 0.01em;
  }
  .wordmark-square {
    background: var(--accent-green);
    flex: none;
  }

  /* details side */
  .card--details .wordmark {
    position: absolute;
    top: 62px;
    left: 0;
    right: 0;
    font-size: 44px;
    line-height: 1;
  }
  .card--details .wordmark-square { width: 26px; height: 26px; }

  .name-band {
    position: absolute;
    top: 144px;
    left: 0;
    right: 0;
    height: 28px;
    background: var(--slate);
    border-top: 3px solid var(--slate-dark);
    display: flex;
    align-items: center;
    justify-content: center;
    color: #fff;
    font-size: 15px;
    white-space: nowrap;
  }
  .name-band .person { font-weight: 700; }
  .name-band .role { font-weight: 400; }

  .details {
    position: absolute;
    top: 186px;
    left: 0;
    right: 0;
    display: flex;
    justify-content: center;
  }
  .address {
    font-style: normal;
    text-align: right;
    font-size: 12.5px;
    line-height: 1.45;
    padding-right: 18px;
    padding-top: 26px;
    white-space: nowrap;
  }
  .address .company { font-weight: 700; }
  .contacts {
    list-style: none;
    border-left: 1px solid var(--slate);
    padding-left: 16px;
    font-size: 12.5px;
    line-height: 1;
    white-space: nowrap;
  }
  .contacts li {
    display: flex;
    align-items: center;
    gap: 8px;
    height: 22px;
  }
  .contacts svg { width: 13px; height: 13px; flex: none; }

  .base-rule {
    position: absolute;
    left: 0;
    right: 0;
    top: 290px;
    height: 4px;
    background: var(--slate);
  }

  /* logo side */
  .card--logo .wordmark {
    position: absolute;
    inset: 0;
    font-size: 92px;
    line-height: 1;
    gap: 22px;
  }
  .card--logo .wordmark-square { width: 52px; height: 52px; }
</style>
</head>
<body>
<main class="canvas">

  <section class="card card--details" aria-label="Business card, details side">
    <div class="wordmark">
      <span class="wordmark-square"></span>
      <span class="wordmark-name">Vexel</span>
    </div>

    <div class="name-band">
      <span class="person">Joel Harcastle,</span>&nbsp;<span class="role">Director</span>
    </div>

    <div class="details">
      <address class="address">
        <div class="company">Vexel Consultants Pty Ltd</div>
        <div>Fernhollow first floor, Tamber Street</div>
        <div>Elmsbury VIC 3199 Australia</div>
      </address>
      <ul class="contacts">
        <li>
          <svg viewBox="0 0 16 16" aria-hidden="true">
            <circle cx="8" cy="8" r="7.5" fill="none" stroke="#5b6470"/>
            <path d="M5.2 4.3l1.4-.3.9 2-1 .8c.5 1.1 1.3 1.9 2.4 2.4l.8-1 2 .9-.3 1.4c-3.5.2-6.4-2.7-6.2-6.2z" fill="#5b6470"/>
          </svg>
          +61 03 9555 0187
        </li>
        <li>
          <svg viewBox="0 0 16 16" aria-hidden="true">
            <circle cx="8" cy="8" r="8" fill="#5b6470"/>
            <rect x="4" y="5.2" width="8" height="5.6" fill="#fff"/>
            <path d="M4 5.2l4 3 4-3" fill="none" stroke="#5b6470" stroke-width="0.9"/>
          </svg>
          mail@vexel-example.com.au
        </li>
        <li>
          <svg viewBox="0 0 16 16" aria-hidden="true">
            <circle cx="8" cy="8" r="8" fill="#5b6470"/>
            <circle cx="8" cy="8" r="4.5" fill="none" stroke="#fff" stroke-width="0.9"/>
            <ellipse cx="8" cy="8" rx="2" ry="4.5" fill="none" stroke="#fff" stroke-width="0.9"/>
            <path d="M3.5 8h9" stroke="#fff" stroke-width="0.9"/>
          </svg>
          www.vexel-example.com.au
        </li>
      </ul>
    </div>

    <div class="base-rule"></div>
  </section>

  <section class="card card--logo" aria-label="Business card, logo side">
    <div class="wordmark">
      <span class="wordmark-square"></span>
      <span class="wordmark-name">Vexel</span>
    </div>
  </section>

</main>
</body>
</html>
```